Building company buisness cards

We are looking for a sharp modern new look for our business cards.
We are a New Zealand based company that specialises in house and land packages.
We have attached a photo of the current logo and would like to see if it can be improved somehow if needed.
We are open to any colours but we have chosen green at this stage.
Feel free to change the font and make the logo smarter looking.
Play with the colours and see what looks best.

We want a card that looks so good know one will want to throw it away!

Target Market(s)

Home buyers

Industry/Entity Type

Building

Contact Information for Business Card

Dorian Keswick
0217392604
dkeswick@tidewellhomecraft.co.nz
tidewellhomecraft.co.nz

Font styles to use
Serif
Sans Serif

Colors

Designer to choose colors to be used in the design.

Requirements
Must have
• Logo and company name on one side, details on the other side
Nice to have
• Color codes for the original green are HEX #4a8028, RGB(74,128,40), CMYK(42,0,69,50)
• Round corners, Raised and/or spot UV

```html
<!DOCTYPE html>
<html lang="en">
<head>
<meta charset="utf-8">
<title>Tidewell Homecraft – Business Cards</title>
<link rel="stylesheet" href="https://fonts.googleapis.com/css2?family=Montserrat:wght@500;600;800&display=swap">
<style>
  :root {
    --stage: #1f1f1f;
    --brand-green: #4a8028;
    --sage: #c9d8c1;
    --sage-deep: #b5c9aa;
    --paper: #ffffff;
    --card-w: 560px;
    --card-h: 320px;
  }
  * { box-sizing: border-box; margin: 0; padding: 0; }
  html, body {
    width: 1200px; height: 900px; overflow: hidden;
    background: var(--stage);
    font-family: "Montserrat", sans-serif;
  }
  .stage { position: relative; width: 1200px; height: 900px; }

  .card {
    position: absolute;
    width: var(--card-w); height: var(--card-h);
    border-radius: 14px;
    overflow: hidden;
    box-shadow: 0 18px 40px rgba(0,0,0,.45);
  }
  .card-details { left: 70px; top: 110px; background: var(--sage); }
  .card-brand   { left: 570px; top: 470px; background: var(--brand-green); }

  .card-bands { position: absolute; inset: 0; width: 100%; height: 100%; }

  /* details side */
  .contact-panel {
    position: absolute; left: 170px; top: 52px;
    width: 330px; height: 230px;
    background: var(--paper);
    border-radius: 26px;
    box-shadow: 0 6px 16px rgba(0,0,0,.12);
    display: flex; flex-direction: column; align-items: center; justify-content: center;
    gap: 6px;
    color: var(--brand-green);
    text-align: center;
  }
  .contact-name { font-weight: 800; font-size: 28px; letter-spacing: -.3px; margin-bottom: 6px; }
  .contact-icon { width: 18px; height: 18px; display: block; }
  .contact-line { font-weight: 500; font-size: 13px; margin-bottom: 4px; }

  /* brand side */
  .brand-lockup {
    position: absolute; left: 56px; top: 118px;
    display: flex; align-items: center; gap: 16px;
    color: var(--paper);
  }
  .brand-dot { width: 22px; height: 22px; border-radius: 50%; background: var(--paper); flex: none; }
  .brand-name { font-weight: 800; font-size: 30px; line-height: 1.05; }
</style>
</head>
<body>
<main class="stage">

  <section class="card card-details" aria-label="Contact side">
    <svg class="card-bands" viewBox="0 0 560 320" aria-hidden="true">
      <polygon points="0,0 200,0 0,200" fill="var(--brand-green)"/>
      <polygon points="0,320 0,290 560,290 560,320" fill="var(--brand-green)"/>
      <polygon points="470,0 560,0 560,90" fill="var(--brand-green)"/>
      <polygon points="40,290 150,60 190,60 80,290" fill="var(--sage-deep)"/>
    </svg>
    <div class="contact-panel">
      <p class="contact-name">Dorian Keswick</p>
      <svg class="contact-icon" viewBox="0 0 20 20" aria-hidden="true">
        <circle cx="10" cy="10" r="10" fill="var(--brand-green)"/>
        <path d="M7 5.5l2 2-1.2 1.4a7 7 0 0 0 3.3 3.3l1.4-1.2 2 2-1.3 1.5c-4 0-8-4-8-8z" fill="var(--paper)"/>
      </svg>
      <p class="contact-line">0217392604</p>
      <svg class="contact-icon" viewBox="0 0 20 20" aria-hidden="true">
        <circle cx="10" cy="10" r="10" fill="var(--brand-green)"/>
        <rect x="5" y="6.5" width="10" height="7" fill="none" stroke="var(--paper)" stroke-width="1.3"/>
        <path d="M5 6.5l5 4 5-4" fill="none" stroke="var(--paper)" stroke-width="1.3"/>
      </svg>
      <p class="contact-line">dkeswick@tidewellhomecraft.co.nz</p>
      <svg class="contact-icon" viewBox="0 0 20 20" aria-hidden="true">
        <circle cx="10" cy="10" r="10" fill="var(--brand-green)"/>
        <circle cx="10" cy="10" r="5" fill="none" stroke="var(--paper)" stroke-width="1.2"/>
        <ellipse cx="10" cy="10" rx="2.2" ry="5" fill="none" stroke="var(--paper)" stroke-width="1.1"/>
        <path d="M5 10h10" stroke="var(--paper)" stroke-width="1.1"/>
      </svg>
      <p class="contact-line">tidewellhomecraft.co.nz</p>
    </div>
  </section>

  <section class="card card-brand" aria-label="Brand side">
    <svg class="card-bands" viewBox="0 0 560 320" aria-hidden="true">
      <polygon points="330,320 450,90 560,90 560,320" fill="var(--paper)"/>
      <polygon points="250,320 330,170 360,170 280,320" fill="var(--paper)" opacity=".9"/>
      <polygon points="180,320 230,230 255,230 205,320" fill="var(--paper)" opacity=".85"/>
    </svg>
    <div class="brand-lockup">
      <span class="brand-dot"></span>
      <p class="brand-name">tidewell<br>homecraft.</p>
    </div>
  </section>

</main>
</body>
</html>
```